Flyer-Design für Brick and Stone Restorator
Zielgruppe
Wir sind Sydneys führender Brick and Stone Restorator.
Aufgabenstellung
Unsere neue webseite geht in ein paar tagen online und wir möchten gerne passenden zur neuen Webseite ein corporate Flyer, letztendlich soll es ein Print Version von unserer neuen Webseite sein. Sprich die wichtigsten Informationen der Webseite soll in dem Flyer enthalten sein. Letztendlich möchte ich designer keine großen einschränkungen geben, weil das ist euer job kreativ sein ;), aber der flyer sollte evtl. so aufgebaut sein das am Ende die leute entweder uns anrufen oder doch auf unsere neue Webseite gehen sprich evtl ein QR- code or what ever.
Unsere Domain ist kestrelvale.com.au, aber damit ihr die neue Webseite schon sehen könnt müsst ihr auf kestrelvale.com.au/ new, falls dieser Link nicht mehr funktionieren sollte, ist sie schon auf der richtigen domain hochgeladen.
Falls ihr irgendwelche Logos Bilder oder sonst was benötigt und diese nicht aus der Webseite entnehmen könnt, schickt einfach eine kurze Naricht, ich beantworte diese so schnell wie möglich ;)
der Flyer soll ein 6 pager sein!!
mit freundlichen Grüßen euer Kestrel Vale Team

```html
<!DOCTYPE html>
<html lang="en">
<head>
<meta charset="utf-8">
<title>Kestrel Vale – Our Services</title>
<link href="https://fonts.googleapis.com/css2?family=Source+Sans+3:wght@400;600;700&display=swap" rel="stylesheet">
<style>
  :root{
    --navy:#221b44;
    --navy-soft:#2c2553;
    --ink:#2a2350;
    --gold:#d9c89a;
    --mist-top:#8f909f;
    --mist-bottom:#d9d8dd;
    --page:#ecebea;
  }
  *{box-sizing:border-box;margin:0;padding:0}
  html,body{width:1200px;height:857px;overflow:hidden;background:var(--page);font-family:"Source Sans 3",sans-serif;color:var(--ink)}
  .spread{position:absolute;left:180px;top:28px;width:840px;height:800px;display:flex;box-shadow:0 6px 24px rgba(0,0,0,.18)}
  .panel{position:relative;width:420px;height:800px;background:linear-gradient(180deg,var(--mist-top),var(--mist-bottom));overflow:hidden}
  .panel + .panel{border-left:1px solid rgba(0,0,0,.12)}
  .band-top{position:absolute;left:0;right:0;top:0;background:var(--navy)}
  .band-bottom{position:absolute;left:0;right:0;bottom:0;height:56px;background:var(--navy-soft)}
  .panel--left .band-top{height:150px}
  .panel--right .band-top{height:160px}
  .panel-title{position:absolute;left:0;right:0;top:56px;text-align:center;color:var(--gold);font-weight:600;font-size:26px;letter-spacing:.3px}
  .skyline{position:absolute;left:0;right:0;background:linear-gradient(180deg,rgba(120,120,140,0) 0%,rgba(95,92,110,.55) 55%,rgba(70,72,90,.7) 70%,rgba(200,195,190,.4) 100%)}
  .panel--left .skyline{top:520px;bottom:56px}
  .panel--right .skyline{top:430px;bottom:56px}
  .services{position:absolute;left:0;right:0;padding:0 28px 0 22px;display:flex;flex-direction:column}
  .panel--left .services{top:190px;gap:20px}
  .panel--right .services{top:190px;gap:18px}
  .service{display:grid;grid-template-columns:74px 1fr;align-items:center;gap:10px}
  .service-icon{width:56px;height:40px;justify-self:center;fill:var(--ink);stroke:var(--ink)}
  .service h3{font-size:14.5px;font-weight:700;line-height:1.1;margin-bottom:2px}
  .service p{font-size:11px;line-height:1.28;text-align:justify}
</style>
</head>
<body>
<main class="spread">
  <section class="panel panel--left">
    <div class="band-top"></div>
    <h2 class="panel-title">Our Services</h2>
    <div class="skyline" role="img" aria-label="Faded photograph of the Sydney harbour skyline at dusk"></div>
    <div class="services">
      <article class="service">
        <svg class="service-icon" viewBox="0 0 56 40"><g stroke="none"><rect x="4" y="26" width="16" height="8"/><rect x="22" y="26" width="16" height="8"/><rect x="12" y="16" width="16" height="8"/><rect x="30" y="16" width="16" height="8"/><rect x="20" y="6" width="16" height="8"/><rect x="38" y="6" width="14" height="8"/></g></svg>
        <div><h3>Brick &amp; Stone Repointing</h3><p>Natural weathering can decay the mortar between your bricks, potentially causing crumbling &amp; rising damp. Repointing is the intricate process of removing decaying mortar &amp; carefully injecting a matching mortar whilst maintaining the original joint profile. Joints are restored using specially formulated KESTREL VALE mortar – greatly improving the appearance and resilience of your building.</p></div>
      </article>
      <article class="service">
        <svg class="service-icon" viewBox="0 0 56 40"><rect x="3" y="14" width="50" height="12" fill="none" stroke-width="3"/><rect x="20" y="17" width="16" height="6" stroke="none"/></svg>
        <div><h3>Tuckpointing</h3><p>Looking to make a feature of the historical character of your building? Tuckpointing is the application of a raised white, black or red line on top of the restored joints. Tuckpointing is an art form that requires skilled craftsmanship. It can provide high definition results - significantly enhancing your building's facade.</p></div>
      </article>
      <article class="service">
        <svg class="service-icon" viewBox="0 0 56 40"><path d="M18 38V16a10 10 0 0 1 20 0v22z" fill="none" stroke-width="2.5"/><path d="M18 24h20M28 6v32" fill="none" stroke-width="2"/></svg>
        <div><h3>Lintel and Arch Bar Replacement</h3><p>Lintels &amp; Arch bars provide the main support structure surrounding your windows, doors &amp; openings. Rusting of bars requires replacement using Kestrel Vale Hot Dipped Galvanised stainless steel or concrete bars - preventing corrosion, bulging and water penetration.</p></div>
      </article>
      <article class="service">
        <svg class="service-icon" viewBox="0 0 56 40"><g stroke="none"><rect x="6" y="14" width="14" height="6"/><rect x="22" y="14" width="12" height="6"/><rect x="6" y="22" width="8" height="6"/><rect x="16" y="22" width="16" height="6"/><rect x="6" y="30" width="14" height="6"/><rect x="22" y="30" width="14" height="6"/><circle cx="40" cy="12" r="9"/></g><path d="M36 12l3 3 5-6" fill="none" stroke="#d9d8dd" stroke-width="2"/></svg>
        <div><h3>Remedial Wall Tie Replacement and Installation</h3><p>Salt can cause the deterioration of wall ties, leaving cavity wall unsupported and compromised if your building is located by the ocean. As a potential alternative to rebuilding walls, KESTREL VALE can install remedial ties using the Torvane Helix system - strengthening and stabilising your building.</p></div>
      </article>
    </div>
    <div class="band-bottom"></div>
  </section>
  <section class="panel panel--right">
    <div class="band-top"></div>
    <div class="skyline" role="img" aria-label="Faded photograph of the Sydney Harbour Bridge and city skyline"></div>
    <div class="services">
      <article class="service">
        <svg class="service-icon" viewBox="0 0 56 40"><path d="M22 34l12-14" fill="none" stroke-width="3"/><path d="M30 16l14-10-4 16z" stroke="none"/></svg>
        <div><h3>Restoring Brick and Stone</h3><p>KESTREL VALE's restoration service is individualised based on your building's needs. Fretted or eroded brickwork can be restored with matching bricks - protecting your buildings integrity for years to come.</p></div>
      </article>
      <article class="service">
        <svg class="service-icon" viewBox="0 0 56 40"><rect x="12" y="18" width="32" height="18" stroke="none"/><path d="M22 18v-5h12v5M18 16l6-10M38 16l-4-10" fill="none" stroke-width="2.5"/></svg>
        <div><h3>Damp Proof Course and Flashing Replacement &amp; Installation</h3><p>KESTREL VALE can repair and install new DPC &amp; Flashing to prevent water damage from damp and moisture. A blocked cavity clean can be provided is required.</p></div>
      </article>
      <article class="service">
        <svg class="service-icon" viewBox="0 0 56 40"><path d="M14 36V22h8l8-8h10v8H30v14z" fill="none" stroke-width="2.5"/><path d="M34 14V4M40 4v10" fill="none" stroke-width="3"/></svg>
        <div><h3>Ventilation Replacement &amp; Installation</h3><p>Vents and weep holes are installed at regular intervals or problem areas to prevent moisture build up. Weep holes are essential and long term in brick facades, yet vents may need replacing due to weather, age and decay.</p></div>
      </article>
      <article class="service">
        <svg class="service-icon" viewBox="0 0 56 40"><path d="M22 12c-5 8-8 12-8 17a8 8 0 0 0 16 0c0-5-3-9-8-17z" fill="none" stroke-width="2.5"/><path d="M36 4c-3 5-5 8-5 11a5 5 0 0 0 10 0c0-3-2-6-5-11z" fill="none" stroke-width="2.5"/></svg>
        <div><h3>Water Repellant</h3><p>Drymar Water Repellant is a clear impregnating water repellant that penetrates and chemically reacts with the surface, preventing deterioration by keeping water out, and allowing moisture to escape. The water repellant is applied after repointing for optimum moisture prevention.</p></div>
      </article>
      <article class="service">
        <svg class="service-icon" viewBox="0 0 56 40"><path d="M16 2v38M40 2v38M10 10h36M10 20h36M10 30h36" fill="none" stroke-width="3"/></svg>
        <div><h3>Scaffolding Service</h3><p>KESTREL VALE can supply and erect our own scaffolding. Our trained staff provide safety compliant platforms for our team to complete works on multi storey, hard to reach or awkward positioned buildings. This allows us to work independently and cost effectively.</p></div>
      </article>
    </div>
    <div class="band-bottom"></div>
  </section>
</main>
</body>
</html>
```